New Logo/Stationery Design Project (Modernisation)

We are a specialist metering company trading for over 60 years and due to the fast moving market we are in have recently developed GPRS metering infrastructure & machine to machine monitoring services. For more information please see http://www.halvard-sons.com/remote-meter-reading.html

Our present logo is poor and outdated; I have a new domain for development of our new e commerce site @ www.halvardmeters.com that will replace the existing site when complete but the present logo looks out of place alongside the new site theme.

Basically need some creative ideas from you guys on tweaking the original logo.

Maybe with some line chart, Cloud or Global network graphics worked into the logo/Stationery relating to our online services.

+ Stationery Design to match please

Thanks
Derek

Dear Designer's                            

We appreciate the work involved on this project and due to approaching deadline have added participation payment and small increase to 1st place payment,  looking forward to getting the designs wrapped up. 

Good luck

Derek

                                   

Electrical Wholesales/ Retailers, Global Utilities, Property letting agencies, Renewable energy companies + end users, Electrical Contractors etc.

It Company

• Basically need some creative ideas from you guys on a great logo.
Maybe with some line chart, Cloud or Global network Graphics worked into the logo relating to our online services.

```html
<!DOCTYPE html>
<html lang="en">
<head>
<meta charset="utf-8">
<title>Halvard &amp; Sons Metering – Stationery</title>
<link rel="stylesheet" href="https://fonts.googleapis.com/css2?family=Roboto+Slab:wght@400&display=swap">
<style>
  :root {
    --backdrop: #e9e9ea;
    --paper: #ffffff;
    --ink: #3a3a3c;
    --brand-blue: #4aa8d8;
    --card-dark: #4a4a4c;
    --on-dark: #ffffff;
    --shadow: rgba(0, 0, 0, 0.12);
  }
  * { box-sizing: border-box; margin: 0; padding: 0; }
  html, body {
    width: 1200px; height: 800px; overflow: hidden;
    background: var(--backdrop);
    font-family: "Roboto Slab", Georgia, serif;
    font-weight: 400;
    color: var(--ink);
  }
  .stationery { position: relative; width: 1200px; height: 800px; }

  .letterhead {
    position: absolute; left: 110px; top: 40px;
    width: 509px; height: 720px;
    background: var(--paper);
    box-shadow: 0 6px 18px var(--shadow);
  }
  .brand {
    display: flex; align-items: center; gap: 10px;
    white-space: nowrap;
  }
  .brand-square {
    flex: none; width: 14px; height: 14px;
    background: var(--brand-blue);
  }
  .brand-name { font-weight: 400; line-height: 1.2; }

  .letterhead .brand { position: absolute; top: 60px; left: 50%; transform: translateX(-50%); }
  .letterhead .brand-name { font-size: 15px; color: var(--ink); }

  .sender-address {
    position: absolute; top: 118px; right: 40px;
    font-style: normal; font-size: 9px; line-height: 1.5; text-align: right;
  }
  .letter-footer {
    position: absolute; left: 0; right: 0; bottom: 0; height: 46px;
    background: var(--brand-blue); color: var(--on-dark);
    display: flex; align-items: center; justify-content: space-between;
    padding: 0 30px; font-size: 8.5px;
  }

  .business-card {
    position: absolute; width: 350px; height: 200px;
    display: flex; align-items: center; justify-content: center;
    box-shadow: 0 6px 18px var(--shadow);
  }
  .business-card--light { left: 720px; top: 150px; background: var(--paper); }
  .business-card--dark { left: 720px; top: 450px; background: var(--card-dark); }
  .business-card .brand-square { width: 16px; height: 16px; }
  .business-card .brand-name { font-size: 17px; }
  .business-card--light .brand-name { color: var(--ink); }
  .business-card--dark .brand-name { color: var(--on-dark); }
</style>
</head>
<body>
<main class="stationery">
  <section class="letterhead" aria-label="Letterhead">
    <div class="brand">
      <span class="brand-square"></span>
      <span class="brand-name">Halvard &amp; Sons Metering UK Ltd</span>
    </div>
    <address class="sender-address">
      14 Mill Lane<br>Thornbury<br>Harwell Park<br>Kendal, LA9 4QT
    </address>
    <footer class="letter-footer">
      <span>Contact: 0161 496 0218</span>
      <span>Email: office@halvardsons.com</span>
      <span>Company No: 0428817</span>
      <span>VAT Reg: 318 276 904</span>
    </footer>
  </section>

  <section class="business-card business-card--light" aria-label="Business card, front">
    <div class="brand">
      <span class="brand-square"></span>
      <span class="brand-name">Halvard &amp; Sons Metering UK Ltd</span>
    </div>
  </section>

  <section class="business-card business-card--dark" aria-label="Business card, back">
    <div class="brand">
      <span class="brand-square"></span>
      <span class="brand-name">Halvard &amp; Sons Metering UK Ltd</span>
    </div>
  </section>
</main>
</body>
</html>
```